Redesign digital storytelling app interface for picking topics and recording/listening to audio

We are building an app for users to tell stories to their friends and family in response to prompts. Our current interface is very basic, and we want to have it redesigned in order to make it more visually appealing and feel more like a comfortable conversation. We also need one screen created from scratch to match the existing screens.
In this app, the user picks a story topic from a list a friend has sent to them and then makes an audio recording in response to that topic. The other user receives the recording and listens to it, then responds to the story.
Attached are images of the screens we want to have redesigned.
1. Topic Selection Screen - screen showing the three prompts that the user will pick from before recording their story.
2. Story Recording Screen - screen that the user sees while recording their story.
3. Playback Screen - screen that the user sees while listening to the story.
4. Respond to Story Screen - screen that the user sees after listening to the story on the playback screen. This screen should have buttons for the user to communicate with the person who sent them the story, including: a quick record button where the user can send a voice message responding to the story, a phone call button, a text button, a velnorix button, and a drumo button. It should also have a button to return to the main menu.
I've also attached a graphic showing what we are currently using for a logo and color scheme. This does not need to be followed exactly.
As an added bonus, please give an example of how to manage these screens when the stories are not one-on-one, but in a group of four people.
The mood of this product should be comfortable, personal, and conversational. We want people to feel like they're chatting with an old friend. The design itself can be anything at all, so go wild!
Digital

```html
<!DOCTYPE html>
<html lang="en">
<head>
<meta charset="utf-8">
<title>Respond to Story — screens</title>
<link rel="stylesheet" href="https://fonts.googleapis.com/css2?family=Roboto:wght@300;400;500&display=swap">
<style>
  :root {
    --page: #ffffff;
    --green-overlay: #2f6a12;
    --green-dim: #13220c;
    --green-app-top: #1c3a12;
    --green-app-bottom: #0f1d0a;
    --green-card: #3d7a1c;
    --green-line: #8fc26a;
    --green-accent: #3a7d21;
    --green-deep: #2f6e1f;
    --white: #ffffff;
    --text-soft: rgba(255,255,255,0.55);
    --label-dark: #555555;
    --control: #23324a;
  }
  * { box-sizing: border-box; margin: 0; padding: 0; }
  html, body { width: 1200px; height: 602px; overflow: hidden; background: var(--page); }
  body { position: relative; font-family: "Roboto", sans-serif; color: var(--white); }

  .screen { position: absolute; top: 61px; width: 270px; height: 480px; overflow: hidden; }
  .screen--overlay { background: var(--green-overlay); }
  .screen--dim { background: var(--green-dim); }
  .screen--app { background: linear-gradient(180deg, var(--green-app-top), var(--green-app-bottom)); }

  .blurred-photo {
    position: absolute; left: 85px; top: 100px; width: 100px; height: 100px; border-radius: 50%;
    background: radial-gradient(circle, rgba(40,40,40,0.55), rgba(40,40,40,0) 70%);
    filter: blur(4px);
  }
  .screen--overlay .blurred-photo { background: radial-gradient(circle, rgba(120,150,110,0.45), rgba(120,150,110,0) 70%); }

  .top-icon { position: absolute; width: 16px; height: 16px; }
  .top-icon svg { width: 100%; height: 100%; }

  .heading { position: absolute; left: 0; right: 0; text-align: center; }
  .heading__kicker { font-size: 10px; font-weight: 500; }
  .heading__name { font-size: 15px; font-weight: 300; margin-top: 6px; letter-spacing: 0.2px; }

  .action { position: absolute; width: 80px; margin-left: -40px; margin-top: -20px; text-align: center; }
  .action__ring {
    display: flex; align-items: center; justify-content: center; margin: 0 auto;
    width: 40px; height: 40px; border-radius: 50%; border: 1px solid var(--green-line);
  }
  .action__ring svg { width: 18px; height: 18px; color: var(--green-line); }
  .action__ring--active { background: var(--white); border-color: var(--white); }
  .action__ring--active svg { color: var(--green-accent); }
  .action__label { display: block; font-size: 8.5px; margin-top: 5px; color: var(--white); }

  .status-bar { position: absolute; top: 0; left: 0; right: 0; height: 20px; font-size: 8.5px; color: var(--text-soft); text-align: right; padding: 5px 10px 0 0; }
  .app-bar { position: absolute; top: 30px; left: 0; right: 0; height: 20px; }
  .app-bar__title { position: absolute; left: 37px; top: 2px; font-size: 12px; color: var(--text-soft); }
  .app-bar__menu { position: absolute; right: 14px; top: 4px; width: 3px; }
  .app-bar__menu i { display: block; width: 2.5px; height: 2.5px; border-radius: 50%; background: var(--text-soft); margin-bottom: 2px; }

  .sound-band {
    position: absolute; left: 0; right: 0; top: 265px; height: 90px;
    background: linear-gradient(180deg, rgba(255,255,255,0), rgba(255,255,255,0.08) 50%, rgba(255,255,255,0));
  }

  .card { position: absolute; left: 25px; top: 70px; width: 219px; height: 341px; }
  .card--green { background: var(--green-card); }
  .card--light { background: var(--white); color: #444; }
  .card__pattern {
    position: absolute; inset: 0;
    background: linear-gradient(180deg, rgba(58,125,33,0.05), rgba(58,125,33,0) 40%, rgba(58,125,33,0.06) 60%, rgba(58,125,33,0));
  }
  .card--light .heading__kicker { color: #444; font-weight: 400; }
  .card--light .heading__name { color: #444; }
  .card--light .action__ring { border-color: var(--green-accent); border-width: 1.5px; }
  .card--light .action__ring svg { color: var(--green-deep); }
  .card--light .action__ring--active { background: var(--green-deep); border-color: var(--green-deep); }
  .card--light .action__ring--active svg { color: var(--white); }
  .card--light .action__label { color: var(--label-dark); }

  .controls { position: absolute; left: 0; right: 0; top: 438px; }
  .control { position: absolute; width: 32px; height: 32px; margin: -16px 0 0 -16px; border-radius: 50%; border: 1px solid rgba(255,255,255,0.12); display: flex; align-items: center; justify-content: center; }
  .control svg { width: 12px; height: 12px; color: rgba(255,255,255,0.18); }
  .control--main { width: 54px; height: 54px; margin: -27px 0 0 -27px; background: var(--control); border: 2px solid #3a4a66; }
  .control--main svg { width: 16px; height: 16px; color: #6d7c98; }
</style>
</head>
<body>

<svg width="0" height="0" style="position:absolute" aria-hidden="true">
  <defs>
    <symbol id="icon-mic" viewBox="0 0 24 24"><g fill="none" stroke="currentColor" stroke-width="1.6" stroke-linecap="round"><rect x="9" y="3" width="6" height="11" rx="3"/><path d="M6 11a6 6 0 0 0 12 0M12 17v4M9 21h6"/></g></symbol>
    <symbol id="icon-phone" viewBox="0 0 24 24"><path fill="none" stroke="currentColor" stroke-width="1.6" stroke-linejoin="round" d="M5 3h4l2 5-2.5 1.5a11 11 0 0 0 6 6L16 13l5 2v4a2 2 0 0 1-2 2A16 16 0 0 1 3 5a2 2 0 0 1 2-2z"/></symbol>
    <symbol id="icon-mail" viewBox="0 0 24 24"><g fill="none" stroke="currentColor" stroke-width="1.6" stroke-linejoin="round"><rect x="3" y="6" width="18" height="12"/><path d="M3 6l9 7 9-7M3 18l7-6M21 18l-7-6"/></g></symbol>
    <symbol id="icon-home" viewBox="0 0 24 24"><path fill="none" stroke="currentColor" stroke-width="1.6" stroke-linejoin="round" d="M3 11l9-7 9 7M5 10v10h5v-6h4v6h5V10"/></symbol>
    <symbol id="icon-back" viewBox="0 0 24 24"><path fill="none" stroke="currentColor" stroke-width="2" stroke-linecap="round" stroke-linejoin="round" d="M20 12H5M11 6l-6 6 6 6"/></symbol>
    <symbol id="icon-close" viewBox="0 0 24 24"><path fill="none" stroke="currentColor" stroke-width="2" stroke-linecap="round" d="M5 5l14 14M19 5L5 19"/></symbol>
    <symbol id="icon-pause" viewBox="0 0 24 24"><path fill="currentColor" d="M6 4h4v16H6zM14 4h4v16h-4z"/></symbol>
    <symbol id="icon-rewind" viewBox="0 0 24 24"><path fill="currentColor" d="M11 6v12L3 12zM21 6v12l-8-6z"/></symbol>
    <symbol id="icon-forward" viewBox="0 0 24 24"><path fill="currentColor" d="M13 6v12l8-6zM3 6v12l8-6z"/></symbol>
    <symbol id="icon-prev" viewBox="0 0 24 24"><path fill="currentColor" d="M5 5h3v14H5zM20 5v14L9 12z"/></symbol>
    <symbol id="icon-next" viewBox="0 0 24 24"><path fill="currentColor" d="M16 5h3v14h-3zM4 5v14l11-7z"/></symbol>
  </defs>
</svg>

<!-- Respond overlay, bright -->
<section class="screen screen--overlay" style="left:18px">
  <div class="blurred-photo" role="img" aria-label="Blurred profile photo of the storyteller"></div>
  <span class="top-icon" style="left:18px;top:21px;color:var(--green-line)"><svg><use href="#icon-back"/></svg></span>
  <span class="top-icon" style="right:18px;top:21px;color:var(--green-line)"><svg><use href="#icon-close"/></svg></span>
  <div class="heading" style="top:44px"><p class="heading__kicker">Respond to:</p><p class="heading__name">Mirela Tosçan</p></div>
  <div class="action" style="left:135px;top:126px"><span class="action__ring"><svg><use href="#icon-mic"/></svg></span><span class="action__label">Record</span></div>
  <div class="action" style="left:135px;top:196px"><span class="action__ring"><svg><use href="#icon-phone"/></svg></span><span class="action__label">Call</span></div>
  <div class="action" style="left:135px;top:266px"><span class="action__ring action__ring--active"><svg><use href="#icon-mail"/></svg></span><span class="action__label">Message</span></div>
  <div class="action" style="left:135px;top:338px"><span class="action__ring"></span><span class="action__label">velnorix</span></div>
  <div class="action" style="left:135px;top:408px"><span class="action__ring"></span><span class="action__label">drumo</span></div>
</section>

<!-- Respond overlay, dim -->
<section class="screen screen--dim" style="left:316px">
  <div class="blurred-photo" role="img" aria-label="Blurred profile photo of the storyteller"></div>
  <span class="top-icon" style="left:18px;top:19px;color:var(--green-line)"><svg><use href="#icon-back"/></svg></span>
  <span class="top-icon" style="right:18px;top:19px;color:var(--green-line)"><svg><use href="#icon-close"/></svg></span>
  <div class="heading" style="top:42px"><p class="heading__kicker">Respond to:</p><p class="heading__name">Mirela Tosçan</p></div>
  <div class="action" style="left:135px;top:125px"><span class="action__ring"><svg><use href="#icon-mic"/></svg></span><span class="action__label">Record</span></div>
  <div class="action" style="left:135px;top:195px"><span class="action__ring"><svg><use href="#icon-phone"/></svg></span><span class="action__label">Call</span></div>
  <div class="action" style="left:135px;top:265px"><span class="action__ring action__ring--active"><svg><use href="#icon-mail"/></svg></span><span class="action__label">Message</span></div>
  <div class="action" style="left:135px;top:337px"><span class="action__ring"></span><span class="action__label">velnorix</span></div>
  <div class="action" style="left:135px;top:407px"><span class="action__ring"></span><span class="action__label">drumo</span></div>
</section>

<!-- Respond card, green -->
<section class="screen screen--app" style="left:614px">
  <div class="status-bar">15:45</div>
  <div class="app-bar">
    <span class="top-icon" style="left:12px;top:2px;color:var(--text-soft)"><svg><use href="#icon-back"/></svg></span>
    <span class="app-bar__title">Hear a Story</span>
    <span class="app-bar__menu"><i></i><i></i><i></i></span>
  </div>
  <div class="sound-band" role="img" aria-label="Faint audio waveform decoration"></div>
  <div class="card card--green">
    <span class="top-icon" style="right:8px;top:7px;width:13px;height:13px;color:var(--green-line)"><svg><use href="#icon-close"/></svg></span>
    <div class="heading" style="top:31px"><p class="heading__kicker">Respond to:</p><p class="heading__name">Mirela Tosçan</p></div>
    <div class="action" style="left:62px;top:114px"><span class="action__ring"><svg><use href="#icon-mic"/></svg></span><span class="action__label">Record</span></div>
    <div class="action" style="left:151px;top:114px"><span class="action__ring"><svg><use href="#icon-phone"/></svg></span><span class="action__label">Call</span></div>
    <div class="action" style="left:58px;top:195px"><span class="action__ring action__ring--active"><svg><use href="#icon-mail"/></svg></span><span class="action__label">Message</span></div>
    <div class="action" style="left:152px;top:194px"><span class="action__ring"></span><span class="action__label">velnorix</span></div>
    <div class="action" style="left:58px;top:274px"><span class="action__ring"></span><span class="action__label">drumo</span></div>
    <div class="action" style="left:154px;top:274px"><span class="action__ring"><svg><use href="#icon-home"/></svg></span><span class="action__label">Home</span></div>
  </div>
  <div class="controls">
    <span class="control" style="left:44px"><svg><use href="#icon-prev"/></svg></span>
    <span class="control" style="left:81px"><svg><use href="#icon-rewind"/></svg></span>
    <span class="control control--main" style="left:135px"><svg><use href="#icon-pause"/></svg></span>
    <span class="control" style="left:187px"><svg><use href="#icon-forward"/></svg></span>
    <span class="control" style="left:225px"><svg><use href="#icon-next"/></svg></span>
  </div>
</section>

<!-- Respond card, light -->
<section class="screen screen--app" style="left:912px">
  <div class="status-bar">15:45</div>
  <div class="app-bar">
    <span class="top-icon" style="left:12px;top:2px;color:var(--text-soft)"><svg><use href="#icon-back"/></svg></span>
    <span class="app-bar__title">Hear a Story</span>
    <span class="app-bar__menu"><i></i><i></i><i></i></span>
  </div>
  <div class="card card--light">
    <div class="card__pattern" role="img" aria-label="Faint pattern of media icons and audio waveform"></div>
    <span class="top-icon" style="right:8px;top:7px;width:13px;height:13px;color:var(--green-deep)"><svg><use href="#icon-close"/></svg></span>
    <div class="heading" style="top:31px"><p class="heading__kicker">Respond to:</p><p class="heading__name">Mirela Tosçan</p></div>
    <div class="action" style="left:62px;top:114px"><span class="action__ring"><svg><use href="#icon-mic"/></svg></span><span class="action__label">Record</span></div>
    <div class="action" style="left:151px;top:114px"><span class="action__ring"><svg><use href="#icon-phone"/></svg></span><span class="action__label">Call</span></div>
    <div class="action" style="left:58px;top:195px"><span class="action__ring action__ring--active"><svg><use href="#icon-mail"/></svg></span><span class="action__label">Message</span></div>
    <div class="action" style="left:152px;top:194px"><span class="action__ring"></span><span class="action__label">velnorix</span></div>
    <div class="action" style="left:58px;top:274px"><span class="action__ring"></span><span class="action__label">drumo</span></div>
    <div class="action" style="left:154px;top:274px"><span class="action__ring"><svg><use href="#icon-home"/></svg></span><span class="action__label">Home</span></div>
  </div>
  <div class="controls">
    <span class="control" style="left:44px"><svg><use href="#icon-prev"/></svg></span>
    <span class="control" style="left:81px"><svg><use href="#icon-rewind"/></svg></span>
    <span class="control control--main" style="left:135px"><svg><use href="#icon-pause"/></svg></span>
    <span class="control" style="left:187px"><svg><use href="#icon-forward"/></svg></span>
    <span class="control" style="left:225px"><svg><use href="#icon-next"/></svg></span>
  </div>
</section>

</body>
</html>
```